Postcard Design

Publicity and Communications
Updates

I had originally uploaded a PPT to show the information on the front and back of the post card. SO I will put the text here. FRONT My LOGO Knight on Horse (Gray) with Gold graphics around it. Key Message: Are your Hunts Tax Deductible? Publicity Package – Show Special: $549 Publicize Your Business – Publicize Your Adventure 1 Press Release (1 Page/300 Words) 1 Interview-Style Feature Article (Up to 800 Words) Price valid through Sept. 15, 2015 Director of Communications is a Hunter - 3 GVO Top Tens – 15 Archery U.S. National Championships & World Records - Articles in 1,000’s of TV& Print Media Outlets Publicity from Pell Row to Local News and Company News Letters | Books | Blogs BACK Bram Lattice Media logo 8153 West Harrow Ln. Suite #617 Tucson, AZ 85718 T. (520) 418-9356 M. (321) 707-3162 Marla.Quenby@BramLattice.example www.BramLattice.example Low Prices – World Class Results People Who Get Ahead, Promote. Member: LMTQ, RJW, PLUV, GTKE, USA Fletchcraft, VMO, OPRD National Awards: QWEL, Corvin Dale, Net Outreach Guild, Silver Lattice Honors Sample Price Schedule Blogs & Newsletters $2.25/word Press Releases - $2.25/word Periodicals & Interviews - $1.71/word -

Hi - The Back still has problems that are easy to fix The Sample Prices heading is not a bullet point of the AWARDS. It should be equal importance / same design as the AWARDS The prices are XX per word so, please move the "word" text after the price (bring it up from the second bullet to the first) Please refer to the last message. It shows the text in terms of Heading and the way that the text for each type of writing service / price has it's own separate line and price per word Thanks! We're close

Target Market(s)

Hunters, hunting industry, high end safaris, high end birding and fishing, see Tamsk, Folquina sites, European traditions; audience is typically 40-70 yr. men and women working in this industry.

Industry/Entity Type

Communications

Colors

Designer to choose colors to be used in the design.

Requirements
Must have
• my logo. Note: I uploaded sketches, but am really open to better graphics and layout. Would like powerful images that are general but high quality reference and an "out of Africa" feel, which I don't think that I have accomplished.
Should not have
• Children and teens

```html
<!DOCTYPE html>
<html lang="en">
<head>
<meta charset="UTF-8">
<title>Bram Lattice Media – Postcard Back</title>
<link href="https://fonts.googleapis.com/css2?family=Open+Sans:ital,wght@0,400;0,600;0,700;1,700&display=swap" rel="stylesheet">
<style>
  :root {
    --gold: #c9832f;
    --ink: #111111;
    --card: #efebe6;
    --card-light: #f6f3ef;
    --card-warm: #e6dfd6;
    --white: #ffffff;
    --dots: #555555;
  }
  * { box-sizing: border-box; margin: 0; padding: 0; }
  html, body {
    width: 1200px; height: 848px; overflow: hidden;
    background: var(--white);
    font-family: "Open Sans", Arial, sans-serif;
    color: var(--ink);
  }
  .postcard {
    position: relative;
    width: 1200px; height: 848px;
    background: var(--card);
    overflow: hidden;
  }
  .backdrop-photo {
    position: absolute; inset: 0;
    background:
      radial-gradient(ellipse 420px 520px at 720px 520px, var(--card-warm) 0%, rgba(230,223,214,0) 70%),
      linear-gradient(180deg, var(--card-light) 0%, var(--card) 55%, var(--card-light) 100%);
  }
  .brand-box {
    position: absolute; left: 0; top: 0;
    width: 297px; height: 160px;
    background: var(--white);
    display: flex; align-items: center; justify-content: center; gap: 12px;
    padding: 0 18px;
  }
  .brand-mark {
    width: 26px; height: 26px; border-radius: 50%;
    background: var(--gold); flex: none;
  }
  .brand-name {
    font-weight: 700; font-size: 25px; line-height: 1.15;
    color: var(--gold);
  }
  .divider {
    position: absolute; left: 464px; top: 0;
    width: 2px; height: 693px;
    background: var(--gold);
  }
  .offer {
    position: absolute; left: 20px; top: 186px; width: 420px;
  }
  .headline {
    color: var(--gold); font-weight: 700;
    font-size: 37px; line-height: 44px;
  }
  .price-schedule { margin-top: 18px; padding-left: 8px; }
  .price-head {
    display: flex; justify-content: space-between;
    font-weight: 700; font-size: 24px; line-height: 36px;
  }
  .price-list { list-style: none; }
  .price-row {
    display: flex; align-items: baseline;
    font-size: 24px; line-height: 35.5px;
  }
  .price-row::before { content: "•"; width: 32px; flex: none; padding-left: 2px; }
  .price-leader {
    flex: 1; margin: 0 6px;
    border-bottom: 1.5px dotted var(--dots);
    transform: translateY(-5px);
  }
  .tagline {
    margin-top: 28px;
    font-weight: 700; font-style: italic; font-size: 22px; line-height: 30px;
  }
  .call {
    color: var(--gold); font-weight: 700;
    font-size: 37px; line-height: 46px;
  }
  .affiliations {
    margin-top: 18px;
    font-size: 17.5px; line-height: 23px;
  }
  .contact {
    position: absolute; left: 482px; top: 44px;
    font-size: 19px; line-height: 22px;
    font-style: normal;
  }
</style>
</head>
<body>
  <div class="postcard">
    <div class="backdrop-photo" role="img" aria-label="Faded photograph of a resting lion on sandy ground, in soft beige tones"></div>

    <div class="brand-box">
      <span class="brand-mark"></span>
      <span class="brand-name">Bram Lattice Media</span>
    </div>

    <div class="divider"></div>

    <section class="offer">
      <h1 class="headline">Low Prices<br>World Class Results</h1>

      <div class="price-schedule">
        <div class="price-head"><span>Sample Price Schedule</span><span>Per Word</span></div>
        <ul class="price-list">
          <li class="price-row"><span>Blogs</span><span class="price-leader"></span><span>$2.25</span></li>
          <li class="price-row"><span>Newsletters</span><span class="price-leader"></span><span>$2.25</span></li>
          <li class="price-row"><span>Press Releases</span><span class="price-leader"></span><span>$2.25</span></li>
          <li class="price-row"><span>Periodicals</span><span class="price-leader"></span><span>$1.71</span></li>
          <li class="price-row"><span>Interviews</span><span class="price-leader"></span><span>$1.71</span></li>
        </ul>
      </div>

      <p class="tagline">People Who Get Ahead, Promote.</p>
      <p class="call">CALL: (520) 418-9356</p>

      <p class="affiliations">Member: LMTQ, RJW, PLUV, GTKE, USA Fletchcraft, VMO, OPRD National Awards: QWEL, Corvin Dale, Net Outreach Guild, Silver Lattice Honors</p>
    </section>

    <address class="contact">
      8153 West Harrow Ln.<br>
      Suite #617 Tucson,<br>
      AZ 85718<br>
      T. (520) 418-9356<br>
      M. (321) 707-3162<br>
      Marla.Quenby@BramLattice.example<br>
      www.BramLattice.example
    </address>
  </div>
</body>
</html>
```